Kestrel Summit 2019 Enemies of the End-Times Church Flyer

We want a church conference flyer designed. We are looking for a professional, yet catchy design that uses our brand colors and logo creatively while communicating key information of the event effectively. <br/>The flyer must include all of the following:<br/>Title: Kestrel Summit 2019<br/>Topic: The Enemies of The End-Times Church <br/>Subtitles: <br/> -How the antichrist raises an army by social behavior engineering. <br/>-How the architects of modern social constructs escaped the church's radar. <br/>-The Holy Spirit's end-times agenda:<br/> The Knock-Out Punch!<br/>Speaker: Prophet Marcus Toliver <br/>Dates/time: December 27, 28 & 29 at 6pm<br/>Location: Halvorn Community Center <br/> 241 Pellham Street <br/> Portland, ME 04102<br/>Contact info: phone: 207-555-0148 <br/>email: contact@brookmeadow.example <br/> www.vutel.example<br/>*The flyer must also include a picture of the speaker and our Vutel logo <br/>Thanks, we look forward to seeing what you come up with!

Colors

Designer to choose colors to be used in the design.

Requirements
Must have
• The flyer must include all of the following:
• Title: Kestrel Summit 2019
• Topic: The Enemies of The End-Times Church
• Subtitles:
• -How the antichrist raises an army by social behavior engineering.
• -How the architects of modern social constructs escaped the church's radar.
• -The Holy Spirit's end-times agenda:
• The Knock-Out Punch!
• Speaker: Prophet Marcus Toliver
• Dates/time: December 27, 28 & 29 at 6pm
• Location: Halvorn Community Center
• 241 Pellham Street
• Portland, ME 04102
• Contact info: phone: 207-555-0148
• email: contact@brookmeadow.example
• www.vutel.example
• *The flyer must also include a picture of the speaker and our Vutel logo
Should not have
• Pictures of crosses or church buildings

```html
<!DOCTYPE html>
<html lang="en">
<head>
<meta charset="utf-8">
<title>Kestrel Summit 2019 – The Enemies of the End-Times Church</title>
<link rel="stylesheet" href="https://fonts.googleapis.com/css2?family=Montserrat:wght@400;500;600;700;800;900&family=Oswald:wght@500;600;700&family=Josefin+Sans:wght@300;400&display=swap">
<style>
  :root{
    --navy:#0f1c3a;
    --navy-deep:#0a1329;
    --orange:#f5821f;
    --white:#ffffff;
    --band:#0b0f1e;
    --blue:#2f5fb8;
    --blue-text:#3d78db;
    --rule:#c9d0e0;
  }
  *{box-sizing:border-box;margin:0;padding:0}
  html,body{width:934px;height:1200px;overflow:hidden;background:var(--navy)}
  .flyer{position:relative;width:934px;height:1200px;overflow:hidden;background:var(--navy);font-family:"Montserrat",sans-serif;color:var(--white)}
  .backdrop-portrait{position:absolute;left:0;top:0;width:934px;height:760px;
    background:radial-gradient(ellipse 360px 380px at 330px 300px,#22345f 0%,#182848 45%,rgba(15,28,58,0) 80%)}
  .brand{position:absolute;left:62px;top:86px;display:flex;align-items:center;gap:10px}
  .brand-mark{width:16px;height:16px;background:var(--white)}
  .brand-name{font-family:"Montserrat",sans-serif;font-weight:700;font-size:42px;letter-spacing:2px;color:var(--white);line-height:1}
  .brand-tagline{position:absolute;left:64px;top:138px;font-family:"Montserrat",sans-serif;font-weight:500;font-size:13px;color:var(--white);letter-spacing:1.2px}
  .date-stem{position:absolute;left:814px;top:0;width:11px;height:62px;background:var(--white)}
  .date-box{position:absolute;left:724px;top:62px;width:168px;height:123px;border:1.5px solid var(--white);text-align:center}
  .date-days{margin-top:15px;font-weight:700;font-size:17px;line-height:20px;color:var(--orange)}
  .date-time{font-weight:800;font-size:48px;line-height:50px;color:var(--white)}
  .date-wave{display:block;margin:0 auto}
  .squiggle{position:absolute}
  .title{position:absolute;right:258px;top:240px;text-align:right;line-height:1}
  .title-main{display:block;font-weight:900;font-size:98px;color:var(--orange);letter-spacing:-1px}
  .title-sub{display:block;font-weight:900;font-size:76px;color:var(--white);margin-top:2px}
  .year-tab{position:absolute;left:690px;top:232px;width:56px;height:164px;background:var(--orange);border-radius:0 28px 28px 0}
  .year-tab span{position:absolute;left:50%;top:50%;transform:translate(-50%,-50%) rotate(-90deg);font-weight:800;font-size:34px;color:var(--navy-deep)}
  .rule{position:absolute;height:1px;background:var(--rule)}
  .topic{position:absolute;left:0;width:934px;top:458px;text-align:center;font-family:"Josefin Sans",sans-serif;font-weight:300;font-size:30px;letter-spacing:3.3px;color:var(--white)}
  .speaker-photo{position:absolute;left:300px;top:580px;width:355px;height:460px;border-radius:180px 180px 0 0;
    background:linear-gradient(180deg,#2c4a94 0%,#3a3f52 45%,#2a2c36 100%)}
  .book-photo{position:absolute;left:664px;top:850px;width:262px;height:260px;border-radius:10px;
    background:linear-gradient(160deg,#2b2f38 0%,#14161c 70%,#8a6a2e 100%);transform:skewY(-14deg)}
  .point{position:absolute;font-weight:500;font-size:18px;line-height:23px;color:var(--white)}
  .point::before{content:"";position:absolute;left:-15px;top:9px;width:6px;height:6px;border-radius:50%;background:var(--orange)}
  .point em{font-style:normal;color:var(--orange)}
  .point-strong{display:block;margin-top:6px;font-weight:900;font-size:29px;line-height:30px;color:var(--white)}
  .speaker-connector{position:absolute;left:0;top:0}
  .speaker-label{position:absolute;left:48px;top:918px;width:132px;height:32px;background:var(--orange);font-family:"Oswald",sans-serif;font-weight:600;font-size:22px;line-height:32px;color:var(--navy-deep);text-align:center;letter-spacing:.5px}
  .speaker-name{position:absolute;left:48px;top:956px;font-family:"Oswald",sans-serif;font-weight:600;font-size:25px;color:var(--orange);letter-spacing:.3px}
  .footer-band{position:absolute;left:0;top:1022px;width:934px;height:178px;background:var(--band)}
  .footer-shape{position:absolute;left:0;top:0}
  .venue{position:absolute;left:48px;top:1056px;font-size:18px;line-height:26px;color:var(--white);font-style:normal}
  .venue-name{font-weight:800;font-size:21px;color:var(--blue-text);margin-bottom:4px;letter-spacing:.3px}
  .contact{position:absolute;left:560px;top:1058px;font-size:18px;line-height:26px;color:var(--white)}
  .contact-heading{font-weight:500;margin-bottom:1px}
  .contact-line{display:flex;align-items:center;gap:9px}
  .contact-phone{font-weight:700}
</style>
</head>
<body>
<div class="flyer">
  <div class="backdrop-portrait" role="img" aria-label="Faint large portrait of the speaker in the background"></div>

  <div class="brand"><span class="brand-mark"></span><span class="brand-name">VUTEL</span></div>
  <div class="brand-tagline">LIGHT FOR EVERY SHORE</div>

  <div class="date-stem"></div>
  <div class="date-box">
    <div class="date-days">DECEMBER<br>27, 28 &amp; 29 AT</div>
    <div class="date-time">6PM</div>
    <svg class="date-wave" width="44" height="16" viewBox="0 0 44 16" fill="none" stroke="#fff" stroke-width="1.6">
      <path d="M2 4 q5 -3 10 0 t10 0 t10 0 t10 0"/><path d="M2 11 q5 -3 10 0 t10 0 t10 0 t10 0"/>
    </svg>
  </div>

  <svg class="squiggle" style="left:0;top:202px" width="34" height="22" viewBox="0 0 34 22" fill="none" stroke="#f5821f" stroke-width="2"><path d="M2 6 q4 -4 8 0 t8 0 t8 0 t8 0"/><path d="M2 15 q4 -4 8 0 t8 0 t8 0 t8 0"/></svg>
  <svg class="squiggle" style="left:0;top:972px" width="34" height="22" viewBox="0 0 34 22" fill="none" stroke="#f5821f" stroke-width="2"><path d="M2 6 q4 -4 8 0 t8 0 t8 0 t8 0"/><path d="M2 15 q4 -4 8 0 t8 0 t8 0 t8 0"/></svg>
  <svg class="squiggle" style="left:640px;top:950px" width="42" height="24" viewBox="0 0 42 24" fill="none" stroke="#f5821f" stroke-width="2"><path d="M2 7 q5 -4 10 0 t10 0 t10 0 t10 0"/><path d="M2 16 q5 -4 10 0 t10 0 t10 0 t10 0"/></svg>

  <h1 class="title"><span class="title-main">KESTREL</span><span class="title-sub">SUMMIT</span></h1>
  <div class="year-tab"><span>2019</span></div>

  <div class="rule" style="left:80px;top:436px;width:762px"></div>
  <div class="rule" style="left:80px;top:491px;width:762px"></div>
  <div class="rule" style="left:125px;top:499px;width:610px"></div>
  <h2 class="topic">THE ENEMIES OF THE END-TIMES CHURCH</h2>

  <div class="speaker-photo" role="img" aria-label="Photo of the speaker seated, wearing a grey blazer over a red sweater, with a striped blue circle behind"></div>
  <div class="book-photo" role="img" aria-label="Black leather-bound Bible lying at an angle"></div>

  <p class="point" style="left:65px;top:628px;width:232px">How the <em>antichrist</em><br><em>raises an army</em> by social behavior engineering.</p>
  <p class="point" style="left:65px;top:737px;width:200px">How the architects of modern social constructs escaped the <em>church's radar</em>.</p>
  <p class="point" style="left:671px;top:628px;width:210px"><em>The Holy Spirit's<br>end-times agenda:</em><span class="point-strong">THE KNOCK-<br>OUT PUNCH!</span></p>

  <svg class="speaker-connector" width="400" height="960" viewBox="0 0 400 960" fill="none">
    <path d="M116 918 V866 H302" stroke="#fff" stroke-width="1.4"/>
    <circle cx="116" cy="908" r="4" fill="#fff"/>
  </svg>
  <div class="speaker-label">SPEAKER</div>
  <div class="speaker-name">PROPHET MARCUS TOLIVER</div>

  <div class="footer-band">
    <svg class="footer-shape" width="934" height="178" viewBox="0 0 934 178">
      <polygon points="500,0 934,28 934,178 420,178" fill="#2f5fb8"/>
    </svg>
  </div>

  <address class="venue">
    <div class="venue-name">HALVORN COMMUNITY CENTER</div>
    241 Pellham Street<br>Portland, ME 04102
  </address>

  <div class="contact">
    <div class="contact-heading">CONTACT INFO:</div>
    <div class="contact-line contact-phone">
      <svg width="14" height="14" viewBox="0 0 14 14"><rect x="0.5" y="0.5" width="13" height="13" rx="2" fill="#fff"/><path d="M4 3.5 l1.5 0 l.7 2 -1 .8 q.9 1.8 2.6 2.6 l.8 -1 2 .7 0 1.5 q-4 .3 -6.6 -3 q-1 -1.9 0 -3.6z" fill="#0b0f1e"/></svg>
      207-555-0148
    </div>
    <div class="contact-line">
      <svg width="14" height="10" viewBox="0 0 14 10"><rect width="14" height="10" rx="1" fill="#fff"/><path d="M1 1 L7 6 L13 1" stroke="#2f5fb8" stroke-width="1.2" fill="none"/></svg>
      contact@brookmeadow.example
    </div>
    <div class="contact-line">
      <svg width="14" height="14" viewBox="0 0 14 14" fill="none" stroke="#fff" stroke-width="1.1"><circle cx="7" cy="7" r="6"/><ellipse cx="7" cy="7" rx="2.6" ry="6"/><path d="M1 7 H13 M2 4 H12 M2 10 H12"/></svg>
      www.vutel.example
    </div>
  </div>
</div>
</body>
</html>
```